The Millwrights Rest pub business card design

I need a business card that's modern and minimalistic. The design on the front I need a forester cutting down a tree but as if drawn roughly with a pencil in black accented in a light brown in places.
Then on the back :-
Dan Pellowe
The Millwrights Rest
42 - 44 Carradine Street
Reading
RG4 2QT
Email - dan@millwrightsrestvale.co.uk
Mobile - 07618459302
Id like the colour of the card to be a cream colour or a off white

```html
<!DOCTYPE html>
<html lang="en">
<head>
<meta charset="utf-8">
<title>The Millwrights Rest – Business Card</title>
<link rel="stylesheet" href="https://fonts.googleapis.com/css2?family=Cinzel:wght@400&family=Quicksand:wght@400&family=Tinos&display=swap">
<style>
  :root {
    --page: #e9e7e3;
    --card-light: #f7f6f4;
    --card-mid: #e4e3e1;
    --green: #1f7a3f;
    --green-dark: #145a2c;
    --ink: #1c1c1c;
    --rule: #9a9a9a;
    --artwork-frame: #1a1a1a;
  }
  * { box-sizing: border-box; margin: 0; padding: 0; }
  html, body {
    width: 1200px; height: 900px; overflow: hidden;
    background: var(--page);
  }
  .canvas {
    position: relative; width: 1200px; height: 900px;
    display: flex; align-items: center; justify-content: center; gap: 40px;
  }
  .card {
    position: relative; width: 520px; height: 300px; overflow: hidden;
    background: radial-gradient(ellipse at 55% 45%, var(--card-light) 0%, var(--card-mid) 100%);
    box-shadow: 0 2px 6px rgba(0,0,0,0.18);
  }
  .card__band { position: absolute; inset: 0; width: 100%; height: 100%; }

  /* Front */
  .front__title {
    position: absolute; top: 50px; right: 40px;
    font-family: "Quicksand", sans-serif; font-weight: 400;
    font-size: 30px; letter-spacing: 0.5px; color: var(--ink);
    white-space: nowrap;
  }
  .front__artwork {
    position: absolute; left: 120px; top: 108px; width: 220px; height: 140px;
    border: 3px solid var(--artwork-frame);
    background: linear-gradient(160deg, #3d4a2a 0%, #5d6b3a 40%, #8a7a58 70%, #4a5230 100%);
  }

  /* Back */
  .back__name {
    position: absolute; top: 34px; right: 34px; text-align: right;
    font-family: "Cinzel", serif; font-weight: 400;
    font-size: 30px; letter-spacing: 1px; color: var(--ink);
  }
  .back__venue {
    position: absolute; top: 78px; right: 34px;
    display: flex; align-items: center; gap: 8px;
    font-family: "Quicksand", sans-serif; font-weight: 400;
    font-size: 15px; letter-spacing: 1px; color: var(--ink);
  }
  .back__venue::before, .back__venue::after {
    content: ""; display: block; width: 34px; height: 1px; background: var(--rule);
  }
  .back__contact {
    position: absolute; top: 122px; left: 40px;
    font-family: "Tinos", serif; font-size: 16px; line-height: 26px; color: var(--ink);
    list-style: none;
  }
</style>
</head>
<body>
<main class="canvas">

  <section class="card card--front">
    <svg class="card__band" viewBox="0 0 520 300" preserveAspectRatio="none" aria-hidden="true">
      <path d="M0,160 C150,230 330,292 520,248 L520,300 L0,300 Z" fill="var(--green-dark)"/>
      <path d="M0,178 C150,245 330,300 520,262 L520,300 L0,300 Z" fill="var(--green)"/>
    </svg>
    <h1 class="front__title">The Millwrights Rest</h1>
    <div class="front__artwork" role="img" aria-label="Pencil sketch of a forester cutting down a tree with a chainsaw"></div>
  </section>

  <section class="card card--back">
    <svg class="card__band" viewBox="0 0 520 300" preserveAspectRatio="none" aria-hidden="true">
      <path d="M0,278 C200,290 380,250 520,170 L520,300 L0,300 Z" fill="var(--green-dark)"/>
      <path d="M0,286 C200,300 390,262 520,186 L520,300 L0,300 Z" fill="var(--green)"/>
    </svg>
    <h2 class="back__name">Dan Pellowe</h2>
    <p class="back__venue">The Millwrights Rest</p>
    <ul class="back__contact">
      <li>42 - 44 Carradine Street</li>
      <li>Reading, RG4 2QT</li>
      <li>dan@millwrightsrestvale.co.uk</li>
      <li>07618459302</li>
    </ul>
  </section>

</main>
</body>
</html>
```